Stationery using new logo for pharmacy and gift shop

We need a letterhead, business card, gift voucher and possibly compliments slip design for our pharmacy and gift shop using our new logo.
The letterhead would need to be produced in both colour (purple and green) and grayscale and the business card would preferably be one-sided, but can be two-sided if this works better with the information it needs to have on it.

We would like a simple and elegant design, but not so simple that it looks like we've done it ourselves on Word. Use of our colours would be great but the letterhead would need to look good if printed on our black and white laser printer. If this is not possible then an additional version for grayscale would be needed.

We would need to receive high quality files that we can work with easily, such as pdf's for the letterhead that we can print instantly or order online as it appears on screen and business cards in jpeg and pdf so we can upload to printing sites.
We would like the vouchers in denominations of £5 and £10 in A5 size in a printable format such as PDF so that we don't have to resize.

Letterhead is for use in correspondence and invoicing to patients, surgeries, traders, customers etc.

Our preferred font is Orkney

Letterhead Info
Address
47 Fenwick Rd.
Cockermouth
Cumbria
CA17 4TW

Tel: (01900) 357148
Fax: (01900) 364057
Website: www.brackenfieldpharmacy.com
Email: patientcare@brackenfieldpharmacy.com

Business Card Info.
As above but email address is: rtkdenholm@postbox-mail.co.uk

Voucher Info.
Small print to state that any change will be paid as a credit note.
Space for a staff member to sign, date and stamp voucher

I have quite a few logo files so please ask if you need more uploaded. Or if you need more information to improve the design then please contact me.

Target Market(s)

Both retail customers and professional colleagues

Industry/Entity Type

Pharmacy

Font styles to use
Other font styles liked:
• orkney

Colors
ffffff
9bcb3c
6b449b

Requirements
Must have
• Must be clear and legible with a professional feel. Must use the logo well and all aspects of the designs should work well together.
• Final files MUST be easy to use for non-computer specialists. I need staff to be able to pull up a letterhead template easily if they are writing a letter or raising an invoice. The business card must be in a format ready to be sent to print.
Nice to have
• Letterhead available in a word processor program like word so that letters can be sent by email as well as print or print and scan.

```html
<!DOCTYPE html>
<html lang="en">
<head>
<meta charset="utf-8">
<title>Brackenfield Pharmacy – Letterhead</title>
<link href="https://fonts.googleapis.com/css2?family=Lato:wght@400;700&display=swap" rel="stylesheet">
<style>
  :root {
    --purple: #6b449b;
    --green: #9bcb3c;
    --white: #ffffff;
    --paper: #f8f8f9;
    --header-grey: #e3e0ea;
    --header-green: #e8f1de;
    --ink: #6a6475;
    --backdrop: #c2b4f2;
  }
  * { box-sizing: border-box; margin: 0; padding: 0; }
  html, body {
    width: 1200px; height: 784px; overflow: hidden;
    background: var(--backdrop);
  }
  .canvas {
    position: relative; width: 1200px; height: 784px;
    display: flex; align-items: center; justify-content: center;
  }
  .letterhead {
    position: relative; width: 525px; height: 742px;
    background: var(--paper);
    box-shadow: 0 6px 24px rgba(80, 50, 150, 0.25);
    font-family: "Lato", sans-serif;
    overflow: hidden;
  }
  .header-art {
    position: absolute; top: 0; right: 0;
    width: 300px; height: 190px;
    background: linear-gradient(105deg, var(--header-green) 0%, var(--header-grey) 45%, var(--header-grey) 100%);
    border-bottom-left-radius: 100% 100%;
  }
  .edge-bar { position: absolute; }
  .edge-bar--purple { background: var(--purple); }
  .edge-bar--green { background: var(--green); }
  .brand {
    position: absolute; top: 32px; left: 40px;
    display: flex; align-items: center; gap: 8px;
  }
  .brand__mark { width: 14px; height: 14px; background: var(--purple); flex: none; }
  .brand__name {
    color: var(--purple); font-weight: 700; font-size: 14px;
    letter-spacing: 0.05em; text-transform: uppercase;
  }
  .contact {
    position: absolute; top: 96px; right: 24px;
    list-style: none;
    color: var(--ink); font-size: 7px; line-height: 1.6;
  }
  .contact__item { display: flex; align-items: center; gap: 4px; }
  .contact__item--plain { padding-left: 9px; }
  .contact__dot {
    width: 5px; height: 5px; border-radius: 50%; background: var(--green); flex: none;
  }
</style>
</head>
<body>
<main class="canvas">
  <article class="letterhead">
    <div class="header-art" role="img" aria-label="Soft green and lilac sweeping header decoration"></div>

    <span class="edge-bar edge-bar--purple" style="left:0;top:0;width:5px;height:18px"></span>
    <span class="edge-bar edge-bar--green" style="left:0;top:22px;width:5px;height:22px"></span>
    <span class="edge-bar edge-bar--purple" style="right:0;top:0;width:5px;height:18px"></span>
    <span class="edge-bar edge-bar--green" style="right:0;top:22px;width:5px;height:22px"></span>
    <span class="edge-bar edge-bar--purple" style="left:0;bottom:0;width:390px;height:5px"></span>
    <span class="edge-bar edge-bar--green" style="right:0;bottom:0;width:127px;height:5px"></span>

    <header class="brand">
      <span class="brand__mark"></span>
      <span class="brand__name">Brackenfield Pharmacy</span>
    </header>

    <ul class="contact">
      <li class="contact__item"><span class="contact__dot"></span>47 Fenwick Rd. Cockermouth Cumbria</li>
      <li class="contact__item contact__item--plain">CA17 4TW</li>
      <li class="contact__item"><span class="contact__dot"></span>(01900) 357148</li>
      <li class="contact__item"><span class="contact__dot"></span>(01900) 364057</li>
      <li class="contact__item"><span class="contact__dot"></span>patientcare@brackenfieldpharmacy.com</li>
      <li class="contact__item"><span class="contact__dot"></span>www.brackenfieldpharmacy.com</li>
    </ul>
  </article>
</main>
</body>
</html>
```